Fence Flyer to Attract More Sales During Winter

We need a new flyer made that we can distribute to residential mailboxes. The flyer is to promote our Winter Fence Sale. We like simply designs, and we would like the flyer to showcase a lot of our fence photos. More of our photos are online at our website at www.mybrindlewoodfence.com - our new address needs to also be featured on the flyer - 574 Quarry rd, Monroe, NC 28117. I do want the words "WINTER FENCE SALE" to be dominate on the flyer with the description "Wood fences starting at $12/FT!" Please look through our Facebook page and our website to gather more photos or information. We are flexible on colors, nothing to fancy - simple flyer design please.

Target Market(s)

Residential homeowners that need a new fence to enclose their yard for safety, security or decorative

Industry/Entity Type

Residential Construction

Font styles to use
Sans Serif

Colors

Designer to choose colors to be used in the design.

Requirements
Must have
• Winter Fence Sale
• Contact information for the business
• "Come visit our outdoor showroom, open 24/7!"
Nice to have
• Photos of our fences - you can find more on our website at www.MyBrindlewoodFence.com or Facebook.com/MapleholtFenceWBT
Should not have
• Flashy designs

```html
<!DOCTYPE html>
<html lang="en">
<head>
<meta charset="utf-8">
<title>Winter Fence Sale Flyer</title>
<link rel="stylesheet" href="https://fonts.googleapis.com/css2?family=Archivo+Black&family=Open+Sans:wght@400;600;700&display=swap">
<style>
  :root {
    --brand-blue: #3a84c9;
    --ink: #111111;
    --paper: #ffffff;
    --band-grey: #c3c3c3;
    --footer: #111111;
    --stage: #eef1f4;
    --wood: #c9a46a;
    --grass: #6a9a3c;
    --soil: #8b5a3c;
  }
  * { box-sizing: border-box; margin: 0; padding: 0; }
  html, body { width: 1200px; height: 1200px; overflow: hidden; background: var(--stage); }
  body { font-family: "Open Sans", sans-serif; color: var(--ink); }

  .flyer {
    position: absolute; left: 176px; top: 0;
    width: 848px; height: 1200px; background: var(--paper); overflow: hidden;
  }

  /* Header */
  .brand { position: absolute; left: 72px; top: 60px; display: flex; align-items: center; gap: 12px; }
  .brand-mark { width: 14px; height: 14px; border-radius: 50%; background: #f29a2e; align-self: flex-start; margin-top: 6px; }
  .brand-name { font-weight: 700; font-size: 22px; color: var(--brand-blue); line-height: 1.1; }
  .brand-phone { font-weight: 700; font-size: 21px; color: var(--ink); line-height: 1.25; }
  .brand-tagline { font-size: 7px; font-weight: 600; margin-top: 6px; }
  .address { position: absolute; left: 544px; top: 66px; height: 66px; border-left: 2px solid var(--ink); padding-left: 18px; }
  .address p { font-weight: 700; font-size: 18px; line-height: 23px; }

  /* Hero */
  .hero { position: absolute; left: 0; top: 182px; width: 848px; height: 465px;
    background: linear-gradient(180deg, #2f4a2a 0%, #5f8f37 22%, #74a842 45%, #b08d5c 62%, #8b5a3c 100%); }
  .hero-title { position: absolute; left: 0; top: 196px; width: 848px; text-align: center;
    font-family: "Archivo Black", sans-serif; font-size: 73px; color: var(--paper); letter-spacing: 1px; line-height: 1; }

  .offer-band { position: absolute; left: 0; top: 647px; width: 848px; height: 53px; background: var(--brand-blue); }
  .offer-band .rule { position: absolute; top: 26px; height: 0; border-top: 1.5px dashed var(--paper); }
  .offer-band .text { position: absolute; left: 71px; top: 10px; color: var(--paper); font-weight: 700; font-size: 28px; letter-spacing: 1.5px; }

  .badge { position: absolute; left: 589px; top: 466px; width: 248px; height: 248px; }
  .badge-text { position: absolute; left: 589px; top: 466px; width: 248px; height: 248px; text-align: center; color: var(--paper); }
  .badge-price { font-family: "Open Sans", sans-serif; font-weight: 700; font-size: 84px; letter-spacing: -4px; line-height: 1; margin-top: 58px; }
  .badge-unit { font-weight: 700; font-size: 33px; letter-spacing: 1px; line-height: 1; margin-top: 4px; padding-left: 12px; }

  /* Gallery */
  .gallery { position: absolute; top: 721px; height: 217px; }
  .gallery.g1 { left: 14px; width: 162px; background: linear-gradient(160deg, #6c8a4a, #cfae78 55%, #a88a5a); }
  .gallery.g2 { left: 190px; width: 289px; background: linear-gradient(170deg, #4d6e3a, #c9ab76 45%, #6f6a5c); }
  .gallery.g3 { left: 494px; width: 162px; background: linear-gradient(170deg, #dfe3e6, #d8bb86 45%, #6f9443); }
  .gallery.g4 { left: 672px; width: 163px; background: linear-gradient(180deg, #9fc3e6, #cdb27c 40%, #4f7d33); }

  /* Showroom call-out */
  .showroom { position: absolute; left: 0; top: 960px; width: 848px; height: 141px; background: var(--band-grey);
    text-align: center; padding-top: 18px; font-family: "Archivo Black", sans-serif; font-size: 37px; line-height: 44px; letter-spacing: 1px; }

  /* Footer */
  .footer { position: absolute; left: 0; top: 1101px; width: 848px; height: 99px; background: var(--footer); color: var(--paper); }
  .footer .rule { position: absolute; left: 0; right: 0; top: 13px; border-top: 1px dashed #8a8a8a; }
  .footer p { font-size: 12px; letter-spacing: 0.8px; line-height: 16px; }
  .footer .visit { position: absolute; left: 37px; top: 33px; }
  .footer .more { position: absolute; right: 39px; top: 33px; text-align: right; }
</style>
</head>
<body>
<main class="flyer">
  <header>
    <div class="brand">
      <span class="brand-mark"></span>
      <div>
        <p class="brand-name">Brindlewood Fence</p>
        <p class="brand-phone">704-555-0148</p>
        <p class="brand-tagline">"Because Good Fences Make Good Neighbors"</p>
      </div>
    </div>
    <div class="address">
      <p>NEW ADDRESS:</p>
      <p>574 Quarry rd,</p>
      <p>Monroe, NC 28117</p>
    </div>
  </header>

  <section>
    <div class="hero" role="img" aria-label="Photo of a new wooden picket gate and split-rail fence around a green lawn"></div>
    <h1 class="hero-title">WINTER FENCE SALE</h1>

    <div class="offer-band">
      <span class="rule" style="left:0;width:56px"></span>
      <span class="text">WOOD FENCES STARTING AT</span>
      <span class="rule" style="left:616px;width:232px"></span>
    </div>

    <svg class="badge" viewBox="0 0 248 248" aria-hidden="true">
      <circle cx="124" cy="124" r="124" fill="var(--paper)"/>
      <circle cx="124" cy="124" r="114" fill="var(--brand-blue)"/>
      <circle cx="124" cy="124" r="104" fill="none" stroke="var(--paper)" stroke-width="1.5" stroke-dasharray="4 3"/>
    </svg>
    <div class="badge-text">
      <p class="badge-price">$12</p>
      <p class="badge-unit">PER FT!</p>
    </div>
  </section>

  <section>
    <div class="gallery g1" role="img" aria-label="Photo of an installer building a wooden privacy fence"></div>
    <div class="gallery g2" role="img" aria-label="Photo of a wooden privacy fence with a double gate beside a driveway"></div>
    <div class="gallery g3" role="img" aria-label="Photo of a scalloped wooden fence along the side of a house"></div>
    <div class="gallery g4" role="img" aria-label="Photo of a long wooden privacy fence in a backyard"></div>
  </section>

  <section class="showroom">
    <p>COME AND VISIT OUR OUTDOOR</p>
    <p>SHOWROOM, OPEN 24/7!</p>
  </section>

  <footer class="footer">
    <span class="rule"></span>
    <div class="visit">
      <p>VISIT US:</p>
      <p>Facebook.com/MapleholtFenceWBT</p>
    </div>
    <div class="more">
      <p>PHOTOS OF FENCES:</p>
      <p>find more on our website at</p>
      <p>www.MyBrindlewoodFence.com</p>
    </div>
  </footer>
</main>
</body>
</html>
```